Brandt WordPress Design Contest

We need a wordpress design that will incorporate a professional color scheme with company logo in a clean layout. The design needs to consider that this will be developed on a responsive theme. Colors are up to the designer - The green of the logo with black, gray or an accent color. Client wants a 'modern' look.

Industry/Entity Type

It Company

Number of Pages Required

1 page

Font styles to use
Serif
Sans Serif

Requirements
Must have
• Navigation: 1) Home 2) All Auctions 3) Real Estate for Sale 4) Services 5) About Us 6) Contact Us
• Colors - a corporate look with professional color scheme. Green of logo + black and gray, or an eggshell/light beige, or any other accent that keeps within a corporate look.
• In header - logo (attached) , and contact info :5127 Old Harrow Lane, Scottsville, KY 42179
• 270-555-3946
• Fax: 270-555-3947
• Email:info@brandtpropertybidhouse.example
• Design will feature a full width (960 px) slideshow - use a stock photo for real estate.
• Widgets in sidebar or where appropriate - 1) Email Signup 2) Message of the Day 3) Upcoming Auctions 4) News&Events blog 5) Testimonials 6) Social media - FB, twitter, youtube, pinterest, google+
• Footer will have company logo, association logos (attached) and contact info, with another widget area if necessary
Nice to have
• use of drop down menu styling - Upcoming Auctions / Online Auctions/ Past Auctions under the "Auction Calendar" menu item

```html
<!DOCTYPE html>
<html lang="en">
<head>
<meta charset="utf-8">
<title>Brandt Real Estate &amp; Auction Co.</title>
<link rel="stylesheet" href="https://fonts.googleapis.com/css2?family=PT+Sans:ital,wght@0,400;0,700;1,400;1,700&display=swap">
<style>
:root{
  --page:#e2e2e2;
  --brown:#a67f5c;
  --green:#0b6b35;
  --green-light:#2f9a4e;
  --green-dark:#08512a;
  --blue-band:#5aa3e8;
  --link-blue:#2a7fd1;
  --panel:#eeeeee;
  --grey-band:#626262;
  --footer:#333333;
  --white:#ffffff;
  --text:#1a1a1a;
  --red:#c8262a;
}
*{margin:0;padding:0;box-sizing:border-box}
html,body{width:1200px;height:2233px;overflow:hidden}
body{background:var(--page);font-family:"PT Sans",sans-serif;color:var(--text);position:relative}
.abs{position:absolute}

/* header */
.header{left:71px;top:18px;width:1061px;height:287px;background:var(--brown);box-shadow:0 3px 6px rgba(0,0,0,.3)}
.logo{left:92px;top:48px;width:355px;height:227px;background:var(--white);border:3px solid var(--green);display:flex;align-items:center;justify-content:center;gap:16px}
.logo-mark{width:34px;height:34px;background:var(--green)}
.logo-name{font-size:74px;font-weight:700;color:var(--green);letter-spacing:1px}
.contact{left:476px;top:48px;font-size:15px;font-weight:700;color:var(--green)}
.contact li{list-style:none;height:25px;display:flex;align-items:center;gap:14px}
.contact svg{width:14px;height:14px}
.find{left:777px;top:125px;font-size:20px;font-weight:700;color:var(--white);display:flex;align-items:center;gap:8px}
.find-s{width:22px;height:22px;background:#d8d8d8;border-radius:4px}
.social{display:flex;gap:8px}
.social span{width:32px;height:32px;border-radius:50%;display:block;border:2px solid rgba(255,255,255,.6)}
.c1{background:#3b5a9a}.c2{background:#26a6e0}.c3{background:#d12a25}.c4{background:#c8232c}.c5{background:#e04a32}
.social-top{left:920px;top:123px}
.search{left:660px;top:173px;width:454px;height:35px;background:var(--white);border:1px solid #ccc;display:flex}
.search input{flex:1;border:0;padding-left:16px;font:13px "PT Sans",sans-serif;color:#999;background:transparent}
.search-btn{width:66px;background:#1e88e5;display:flex;align-items:center;justify-content:center}
.nav{left:470px;top:220px;width:644px;height:60px;background:linear-gradient(#3ea55a,var(--green-dark));display:flex}
.nav a{color:var(--white);text-decoration:none;font-size:17px;display:flex;align-items:center;justify-content:center;border-right:1px solid rgba(255,255,255,.3);gap:12px}
.nav a:last-child{border-right:0}

/* hero */
.hero{left:79px;top:305px;width:1045px;height:463px;background:linear-gradient(160deg,#c8d6e4 0%,#8fa6bd 40%,#5b6b7c 75%,#3c4652 100%)}
.hero-arrow{width:36px;height:36px;top:491px}

/* intro */
.intro{left:79px;top:768px;width:1045px;height:404px;background:var(--white)}
.overview{left:146px;top:808px;font-size:30px;font-weight:700;line-height:41.5px;color:var(--text)}
.motd{left:170px;top:1008px;width:482px;height:128px;background:#c6c6c6;border:1px solid #aaa;border-radius:6px;text-align:center;color:var(--green);font-style:italic}
.motd h3{font-size:25px;padding-top:14px}
.motd p{font-size:14px;line-height:21px}

.join{left:779px;top:794px;width:315px;height:276px;background:var(--panel);border:1px solid #d3d3d3;box-shadow:0 1px 3px rgba(0,0,0,.2)}
.join h3{text-align:center;color:var(--green);font-size:22px;padding-top:2px;height:38px;border-bottom:1px solid #d0d0d0;margin:0 10px}
.field{left:798px;width:279px;height:44px;background:#e4e4e4;border:1px solid #c8c8c8;display:flex;align-items:center;gap:16px;padding-left:18px;font-size:15px;color:#777}
.btn{left:799px;width:278px;height:51px;background:linear-gradient(#3da558,var(--green-dark));border-radius:3px;color:var(--white);display:flex;align-items:center;padding-left:10px;font-size:24px}
.btn span{flex:1;text-align:center}

.calendar{left:779px;top:1083px;width:315px;height:195px;background:linear-gradient(135deg,#7b8a80,#39413d 60%,#2a302d)}
.cal-select{left:800px;top:1093px;width:278px;height:49px;background:linear-gradient(#dfe6e0,#b4bdb6);border:1px solid #999;border-radius:3px;display:flex;align-items:center;padding:0 14px;gap:26px;font-size:17px;color:var(--red)}
.cal-item{left:800px;width:278px;height:37px;background:rgba(220,225,220,.55);border:1px solid rgba(255,255,255,.3);display:flex;align-items:center;gap:20px;padding-left:16px;font-size:13px;font-weight:700;color:#1e1e1e}

/* blue band */
.band{left:79px;top:1172px;width:1045px;height:372px;background:var(--blue-band)}
.blog{left:104px;top:1213px;width:626px;height:295px;background:var(--panel);border:1px solid #ccc}
.blog h2{position:absolute;left:12px;top:6px;font-size:25px;color:var(--green)}
.post{width:190px;top:1276px}
.post .pic{width:104px;height:104px;border-radius:50%;margin:0 auto;background:linear-gradient(#a8c7e6,#6d86a1 60%,#5a6a55);border:2px solid #fff}
.post h4{font-size:17px;font-style:italic;color:var(--green);margin-top:10px;text-align:left}
.post p{font-size:11px;line-height:13.5px;color:#222}
.post .more{text-align:right;color:var(--link-blue);font-size:11px;margin-top:6px}
.upcoming{left:756px;top:1216px;width:338px;height:291px;background:var(--white);border:1px solid #ccc}
.up-item{left:763px;display:flex;gap:12px;width:324px;align-items:center}
.num{width:32px;height:32px;border-radius:50%;background:var(--green-dark);color:var(--white);font-weight:700;font-size:20px;display:flex;align-items:center;justify-content:center;flex:none}
.up-item p{font-size:12px;line-height:18px;color:var(--link-blue);font-weight:700}
.view-all{left:1006px;top:1478px;width:72px;height:22px;background:var(--green-dark);border-radius:4px;color:var(--white);font-size:12px;font-weight:700;display:flex;align-items:center;justify-content:center}

/* testimonials */
.clients{left:79px;top:1544px;width:1045px;height:298px;background:var(--grey-band)}
.clients h2{position:absolute;left:26px;top:12px;color:var(--white);font-size:25px}
.avatar{width:110px;height:110px;border-radius:50%;background:linear-gradient(#e4e7ea,#9aa0a6);border:2px solid #ddd;top:1627px}
.quote{width:356px;top:1636px;color:var(--white);font-size:14px;font-style:italic;line-height:24px}
.who{color:var(--white);font-size:12px;font-style:italic;text-align:right}
.dots{left:567px;top:1809px;display:flex;gap:13px}
.dots span{width:15px;height:15px;border-radius:50%;background:var(--white)}
.dots .on{background:var(--green)}

/* footer */
.footer{left:79px;top:1842px;width:1045px;height:366px;background:var(--footer)}
.f-logo{left:104px;top:1861px;width:432px;height:325px;background:var(--white);border:4px solid var(--green);display:flex;align-items:center;justify-content:center;gap:20px}
.f-logo .logo-name{font-size:96px}
.f-logo .logo-mark{width:44px;height:44px}
.rights{left:557px;top:1862px;color:var(--white);font-size:13px}
.badges{left:557px;top:1896px;width:360px;height:71px;background:#d0d0d0;display:flex;align-items:center;justify-content:space-around;padding:0 14px}
.badges span{display:block;background:#2a2a2a}
.f-contact{left:574px;top:1986px;width:298px;color:var(--white)}
.f-contact h3{font-size:20px;border-bottom:1px solid #888;padding-bottom:2px;margin-bottom:12px}
.f-contact li{list-style:none;font-size:13px;height:25.4px}
.social-foot{left:948px;top:1860px;gap:5px}
.social-foot span{width:23px;height:23px;border-width:1px}
.f-links{left:956px;top:1893px;color:var(--white);font-size:13px;line-height:18.6px}
.f-links li{list-style:none}
</style>
</head>
<body>

<header class="abs header"></header>
<div class="abs logo"><span class="logo-mark"></span><span class="logo-name">Brandt</span></div>

<ul class="abs contact">
  <li><svg viewBox="0 0 14 14"><rect width="14" height="14" fill="#d9d9d9"/><path d="M7 3a3 3 0 0 0-3 3c0 2 3 5 3 5s3-3 3-5a3 3 0 0 0-3-3z" fill="#555"/></svg>5127 Old Harrow Lane, Scottsville, KY 42179</li>
  <li><svg viewBox="0 0 14 14"><rect width="14" height="14" fill="#d9d9d9"/><path d="M4 3h2l1 2-1 1a6 6 0 0 0 2 2l1-1 2 1v2c-4 0-7-3-7-7z" fill="#555"/></svg>270-555-3946</li>
  <li><svg viewBox="0 0 14 14"><rect x="2" y="5" width="10" height="6" fill="#555"/><rect x="4" y="2" width="6" height="4" fill="#ccc"/></svg>Fax: 270-555-3947</li>
  <li><svg viewBox="0 0 14 14"><rect x="1" y="3" width="12" height="8" fill="#d9d9d9"/><path d="M1 3l6 5 6-5" stroke="#555" fill="none"/></svg>info@brandtpropertybidhouse.example</li>
</ul>

<div class="abs find"><span class="find-s"></span>Find us on:</div>
<div class="abs social social-top"><span class="c1"></span><span class="c2"></span><span class="c3"></span><span class="c4"></span><span class="c5"></span></div>

<div class="abs search"><input type="text" value="Type what you want to search.." aria-label="Search"><span class="search-btn"><svg width="18" height="18" viewBox="0 0 18 18"><circle cx="7" cy="7" r="5" stroke="#fff" stroke-width="2.5" fill="none"/><path d="M11 11l5 5" stroke="#fff" stroke-width="2.5"/></svg></span></div>

<nav class="abs nav">
  <a href="#" style="width:70px" aria-label="Home"><svg width="28" height="24" viewBox="0 0 28 24"><path d="M14 2L2 13h4v9h6v-6h4v6h6v-9h4z" fill="#fff"/></svg></a>
  <a href="#" style="width:137px">All Auctions <svg width="12" height="8" viewBox="0 0 12 8"><path d="M1 1l5 5 5-5" stroke="#fff" stroke-width="2" fill="none"/></svg></a>
  <a href="#" style="width:161px">Real Estate for Sale</a>
  <a href="#" style="width:84px">Services</a>
  <a href="#" style="width:88px">About Us</a>
  <a href="#" style="width:104px">Contact Us</a>
</nav>

<div class="abs hero" role="img" aria-label="Slideshow photo of glass office towers against a pale sky"></div>
<svg class="abs hero-arrow" style="left:104px" viewBox="0 0 36 36"><circle cx="18" cy="18" r="16" fill="none" stroke="#fff" stroke-width="2"/><path d="M21 10l-8 8 8 8" stroke="#fff" stroke-width="2.5" fill="none"/></svg>
<svg class="abs hero-arrow" style="left:1060px" viewBox="0 0 36 36"><circle cx="18" cy="18" r="16" fill="none" stroke="#fff" stroke-width="2"/><path d="M15 10l8 8-8 8" stroke="#fff" stroke-width="2.5" fill="none"/></svg>

<section class="abs intro"></section>
<p class="abs overview">Company Overview Company Overview<br>Company Overview Company Overview<br>Company Overview Company Overview<br>Company Overview Company Overview</p>
<div class="abs motd">
  <h3>Message of the day</h3>
  <p>Lorem ipsum dolor sit amet, consectetur adipiscing elit. Curabitur<br>Lorem ipsum dolor sit amet, consectetur adipiscing elit. Curabitur<br>Lorem ipsum dolor sit amet, consectetur adipiscing elit. Curabitur</p>
</div>

<div class="abs join"><h3>Join Brandt</h3></div>
<div class="abs field" style="top:844px"><svg width="22" height="16" viewBox="0 0 22 16"><rect x="1" y="1" width="20" height="14" fill="none" stroke="#999" stroke-width="2"/><path d="M1 1l10 8 10-8" stroke="#999" stroke-width="2" fill="none"/></svg>Email</div>
<div class="abs field" style="top:888px"><svg width="22" height="20" viewBox="0 0 22 20"><rect x="4" y="8" width="14" height="11" fill="#999"/><path d="M7 8V5a4 4 0 0 1 8 0v3" stroke="#999" stroke-width="2" fill="none"/></svg>Password</div>
<div class="abs btn" style="top:945px"><svg width="24" height="24" viewBox="0 0 24 24"><circle cx="12" cy="12" r="10" fill="none" stroke="#fff" stroke-width="2"/><path d="M9 7l6 5-6 5" stroke="#fff" stroke-width="2" fill="none"/></svg><span style="font-weight:700">Login</span></div>
<div class="abs btn" style="top:1000px"><svg width="24" height="24" viewBox="0 0 24 24"><circle cx="12" cy="12" r="10" fill="none" stroke="#fff" stroke-width="2"/><path d="M12 7v10M7 12h10" stroke="#fff" stroke-width="2"/></svg><span>Create New Account</span></div>

<section class="abs band"></section>
<div class="abs blog"><h2>Recent Blog Posts</h2></div>
<article class="abs post" style="left:112px"><div class="pic" role="img" aria-label="City skyline photo"></div><h4>Latest News &amp; Events 01</h4><p>Lorem ipsum dolor sit amet<br>Lorem ipsum dolor sit amet, consectet<br>Lorem ipsum dolor sit amet, consectet<br>Lorem ipsum dolor sit amet, consectet</p><p class="more">Continue ......</p></article>
<article class="abs post" style="left:320px"><div class="pic" role="img" aria-label="City skyline photo"></div><h4>Latest News &amp; Events 01</h4><p>Lorem ipsum dolor sit amet, consectet<br>Lorem ipsum dolor sit amet,<br>Lorem ipsum dolor sit amet, consectet<br>Lorem ipsum dolor sit amet, consectet</p><p class="more">Continue ......</p></article>
<article class="abs post" style="left:528px"><div class="pic" role="img" aria-label="City skyline photo"></div><h4>Latest News &amp; Events 01</h4><p>Lorem ipsum dolor sit amet, consectet<br>Lorem ipsum dolor sit amet, consectet<br>Lorem ipsum dolor sit amet,<br>Lorem ipsum dolor sit amet, consectet</p><p class="more">Continue ......</p></article>

<div class="abs upcoming"></div>
<div class="abs up-item" style="top:1288px"><span class="num">1</span><p>Lorem ipsum dolor sit amet, consectetur adipiscing<br>Lorem ipsum dolor sit amet, consectetur adipiscing<br>Lorem ipsum dolor sit amet.</p></div>
<div class="abs up-item" style="top:1350px"><span class="num">2</span><p>Lorem ipsum dolor sit amet, consectetur adipiscing<br>Lorem ipsum dolor sit amet, consectetur adipiscing<br>Lorem ipsum dolor sit amet, consectetur.</p></div>
<div class="abs up-item" style="top:1412px"><span class="num">3</span><p>Lorem ipsum dolor sit amet, consectetur adipiscing<br>Lorem ipsum dolor sit amet, consectetur adipiscing<br>Lorem ipsum dolor.</p></div>
<div class="abs view-all">View All</div>

<div class="abs calendar"></div>
<div class="abs cal-select"><svg width="18" height="18" viewBox="0 0 18 18"><rect x="1" y="3" width="16" height="14" fill="none" stroke="#999" stroke-width="1.5"/><path d="M1 7h16" stroke="#999" stroke-width="1.5"/></svg><span style="flex:1">Auction Calendar</span><svg width="12" height="8" viewBox="0 0 12 8"><path d="M1 1l5 5 5-5" stroke="#666" stroke-width="1.5" fill="none"/></svg></div>
<div class="abs cal-item" style="top:1153px"><svg width="18" height="18" viewBox="0 0 18 18"><circle cx="9" cy="9" r="7" fill="none" stroke="#bbb" stroke-width="1.5"/><path d="M9 5v4l3 2" stroke="#bbb" stroke-width="1.5" fill="none"/></svg>Upcomming Auctions</div>
<div class="abs cal-item" style="top:1193px"><svg width="18" height="18" viewBox="0 0 18 18"><rect x="2" y="3" width="14" height="11" fill="none" stroke="#bbb" stroke-width="1.5"/></svg>Online Auctions</div>
<div class="abs cal-item" style="top:1233px"><svg width="18" height="18" viewBox="0 0 18 18"><rect x="1" y="3" width="16" height="14" fill="none" stroke="#bbb" stroke-width="1.5"/><path d="M1 7h16" stroke="#bbb" stroke-width="1.5"/></svg>Past Auctions</div>

<section class="abs clients"><h2>What Client’s Say</h2></section>
<div class="abs avatar" style="left:104px" role="img" aria-label="Portrait of a client"></div>
<p class="abs quote" style="left:235px">Lorem ipsum dolor sit amet, consectetur adipiscing elit. Curabitur non bibendum leo. Ut blandit in leo sit amet . Nibh tellus efficitur magna, at blandit nibh ligula eu mi. Suspendisse fermentum, nisl eget accumsan posuere.</p>
<p class="abs who" style="left:380px;top:1753px;width:200px">Delia, Ferncourt, VIC</p>
<div class="abs avatar" style="left:617px" role="img" aria-label="Portrait of a client"></div>
<p class="abs quote" style="left:747px">Lorem ipsum dolor sit amet, consectetur adipiscing elit. Curabitur non bibendum leo. Ut blandit in leo sit amet. Nibh tellus efficitur magna, at blandit nibh ligula eu mi. Suspendisse fermentum, nisl eget accumsan posuere.</p>
<p class="abs who" style="left:860px;top:1745px;width:200px">Owen, Marsh Vale, NSW</p>
<div class="abs dots"><span></span><span></span><span class="on"></span><span></span><span></span></div>

<footer class="abs footer"></footer>
<div class="abs f-logo"><span class="logo-mark"></span><span class="logo-name">Brandt</span></div>
<p class="abs rights">© All Rights Reserved 2015</p>
<div class="abs badges"><span style="width:90px;height:40px"></span><span style="width:100px;height:44px;border-radius:50%"></span><span style="width:100px;height:48px"></span></div>
<div class="abs f-contact">
  <h3>Contact Us</h3>
  <ul>
    <li>- 5127 Old Harrow Lane, Scottsville, KY 42179</li>
    <li>- 270-555-3946</li>
    <li>- Fax: 270-555-3947</li>
    <li>- Email:info@brandtpropertybidhouse.example</li>
  </ul>
</div>
<div class="abs social social-foot"><span class="c1"></span><span class="c2"></span><span class="c3"></span><span class="c4"></span><span class="c5"></span></div>
<ul class="abs f-links">
  <li>Home</li><li>All Auctions</li><li>Real Estate for Sale</li><li>Services</li><li>About Us</li><li>Privacy Policy</li><li>Join Now</li>
</ul>

</body>
</html>
```